Meditation for IVF and infertility

I need a flyer inviting IVF patients to join my Meditation class, I would like to offer free meditation to ivf women and for couples this class is free every Thursday night at 5 pm
2437 west harlow ave suite K Santa Barbara Ca 93142
quillbrook-stillness.com for more details

```html
<!DOCTYPE html>
<html lang="en">
<head>
<meta charset="utf-8">
<title>Free Meditation Classes for IVF and Infertility</title>
<link rel="stylesheet" href="https://fonts.googleapis.com/css2?family=Questrial&family=Open+Sans:wght@400;600&display=swap">
<style>
  :root {
    --slate: #6c6d70;
    --slate-dark: #5e5f62;
    --lilac: #b7a3b5;
    --white: #ffffff;
    --ink: #5a5a5c;
    --photo-wall: #8a8886;
    --photo-wood: #a57c5a;
    --photo-floor: #c9c6c2;
  }
  html, body {
    margin: 0;
    padding: 0;
    width: 1011px;
    height: 1200px;
    overflow: hidden;
    background: var(--slate);
  }
  .flyer {
    position: relative;
    width: 1011px;
    height: 1200px;
    overflow: hidden;
    font-family: "Open Sans", Arial, sans-serif;
    color: var(--white);
  }
  .flyer__shapes {
    position: absolute;
    inset: 0;
    display: block;
  }
  .brand {
    position: absolute;
    left: 711px;
    top: 395px;
    width: 236px;
    height: 236px;
    border: 3px solid var(--white);
    border-radius: 50%;
    box-sizing: border-box;
    display: flex;
    align-items: center;
    justify-content: center;
    text-align: center;
    font-family: "Questrial", Arial, sans-serif;
    font-size: 30px;
    line-height: 1.1;
    color: var(--white);
  }
  .headline {
    position: absolute;
    left: 0;
    right: 0;
    top: 680px;
    margin: 0;
    text-align: center;
    font-family: "Questrial", Arial, sans-serif;
    font-weight: 400;
    font-size: 60px;
    line-height: 78px;
    color: var(--white);
  }
  .subline {
    position: absolute;
    left: 0;
    right: 0;
    top: 855px;
    margin: 0;
    text-align: center;
    font-size: 18px;
  }
  .schedule {
    position: absolute;
    left: 145px;
    top: 898px;
    width: 717px;
    height: 44px;
    border-radius: 22px;
    background: var(--lilac);
    text-align: center;
    font-size: 26px;
    font-weight: 600;
    line-height: 44px;
    letter-spacing: 0.3px;
  }
  .location {
    position: absolute;
    left: 0;
    right: 0;
    top: 970px;
    margin: 0;
    text-align: center;
    font-size: 22px;
    line-height: 30px;
  }
  .contact {
    position: absolute;
    right: 36px;
    top: 1100px;
    margin: 0;
    padding: 0;
    list-style: none;
    text-align: right;
    font-size: 21px;
    line-height: 30px;
    color: var(--ink);
  }
  .contact__item {
    display: flex;
    justify-content: flex-end;
    align-items: center;
    gap: 8px;
  }
  .contact__icon {
    width: 20px;
    height: 20px;
    flex: none;
  }
</style>
</head>
<body>
<main class="flyer">
  <svg class="flyer__shapes" viewBox="0 0 1011 1200" width="1011" height="1200" aria-hidden="false">
    <defs>
      <linearGradient id="photoTone" x1="0" y1="0" x2="1" y2="0.4">
        <stop offset="0" stop-color="var(--photo-wall)"/>
        <stop offset="0.55" stop-color="#7c7a78"/>
        <stop offset="0.75" stop-color="var(--photo-wood)"/>
        <stop offset="1" stop-color="var(--photo-floor)"/>
      </linearGradient>
    </defs>
    <rect class="panel" width="1011" height="1200" fill="var(--slate)"/>
    <path class="photo" role="img" aria-label="Photo of a row of people sitting cross-legged on mats, meditating in a studio with a wood-panelled wall"
          d="M0 0 H1011 V243 C600 330 300 470 0 475 Z" fill="url(#photoTone)"/>
    <path class="wave" d="M0 475 C300 470 600 330 1011 243 V290 C950 300 870 325 750 390 C550 500 250 680 0 615 Z" fill="var(--lilac)"/>
    <path class="corner-edge" d="M1011 1038 C790 1048 600 1112 425 1200 H1011 Z" fill="var(--lilac)"/>
    <path class="corner" d="M1011 1050 C800 1062 625 1122 465 1200 H1011 Z" fill="var(--white)"/>
  </svg>

  <div class="brand">Quillbrook<br>Stillness</div>

  <h1 class="headline">Free Meditation Classes<br>for IVF and infertility</h1>
  <p class="subline">Free meditation to ivf women and for couples.</p>
  <div class="schedule">EVERY THURSDAY NIGHT AT 5 PM</div>
  <p class="location">2437 west harlow ave suite K Santa Barbara Ca 93142<br>quillbrook-stillness.com for more details</p>

  <ul class="contact">
    <li class="contact__item">(805) 555-0172
      <svg class="contact__icon" viewBox="0 0 20 20"><circle cx="10" cy="10" r="9" fill="var(--ink)"/><path d="M7 5.5 L8.6 5.3 L9.3 7.6 L8.3 8.4 C8.9 9.8 10.1 11 11.5 11.6 L12.3 10.6 L14.6 11.3 L14.4 12.9 C10 13.3 6.6 9.9 7 5.5 Z" fill="var(--white)"/></svg>
    </li>
    <li class="contact__item">hello@quillbrook-stillness.com
      <svg class="contact__icon" viewBox="0 0 20 20"><circle cx="10" cy="10" r="9" fill="var(--ink)"/><rect x="5" y="6.5" width="10" height="7" fill="none" stroke="var(--white)" stroke-width="1.3"/><path d="M5 6.5 L10 10.5 L15 6.5" fill="none" stroke="var(--white)" stroke-width="1.3"/></svg>
    </li>
    <li class="contact__item">www.quillbrook-stillness.com
      <svg class="contact__icon" viewBox="0 0 20 20"><circle cx="10" cy="10" r="9" fill="var(--ink)"/><circle cx="10" cy="10" r="5.5" fill="none" stroke="var(--white)" stroke-width="1.1"/><ellipse cx="10" cy="10" rx="2.4" ry="5.5" fill="none" stroke="var(--white)" stroke-width="1.1"/><path d="M4.5 10 H15.5" stroke="var(--white)" stroke-width="1.1"/></svg>
    </li>
  </ul>
</main>
</body>
</html>
```